Quillfern Nightclub Flyer (Updated)

Flyer for facebook, square is fine, or rectangular. Here is the text:
QUILLFERN
Nightclub + Lounge
presents

SPLIT DECK WEDNESDAY
Nov 29 2018

CLUB FLOOR:
GORDY B2B RALPH
THEODORE BRUSKVIK

LOUNGE:
OTIS B2B HALF TIDE
COPPER FENWICK

Powered by HALVERN Acoustics
4716 Larchmere Avenue 21+ 9pm-2am
quillfernvenue-example.com for VIP booth inquiries

Target Market(s)

Nightclub

Industry/Entity Type

Night Club

Font styles to use
Sans Serif

Colors

Designer to choose colors to be used in the design.

Requirements
Must have
• All the text listed, and plz keep the theme of the attached files. We want to stay consistent with the Quillfern brand
Nice to have
• Try to stay with the theme from the attachments
Should not have
• Dont' stray to far from the general theme we have from the attachments

```html
<!DOCTYPE html>
<html lang="en">
<head>
<meta charset="utf-8">
<title>Quillfern Nightclub + Lounge — Split Deck Wednesday</title>
<link rel="stylesheet" href="https://fonts.googleapis.com/css2?family=Playfair+Display:wght@400;700;800&family=Montserrat:wght@300;400;500;600&display=swap">
<style>
  :root {
    --bg-light: #e8e9eb;
    --bg-dark: #d6d7d9;
    --ink: #161616;
    --ink-soft: #2a2a2a;
    --gold-light: #ecc48a;
    --gold: #c9a06a;
    --gold-deep: #a88456;
    --rule: #b9a88f;
    --white: #ffffff;
  }
  * { margin: 0; padding: 0; box-sizing: border-box; }
  html, body { width: 1200px; height: 1200px; overflow: hidden; }
  .flyer {
    position: relative;
    width: 1200px;
    height: 1200px;
    overflow: hidden;
    background: linear-gradient(135deg, var(--bg-light) 0%, #e1e2e4 50%, var(--bg-dark) 100%);
    color: var(--ink);
    font-family: "Montserrat", sans-serif;
  }
  .brand {
    position: absolute;
    top: 88px;
    left: 0;
    width: 100%;
    text-align: center;
  }
  .brand-name {
    font-family: "Playfair Display", serif;
    font-weight: 400;
    font-size: 88px;
    line-height: 1;
    letter-spacing: 2px;
    color: var(--ink);
  }
  .brand-tagline {
    margin-top: 14px;
    font-weight: 300;
    font-size: 26px;
    letter-spacing: 6px;
    color: var(--ink-soft);
  }
  .divider {
    position: absolute;
    top: 255px;
    left: 544px;
    width: 112px;
    height: 1px;
    background: var(--rule);
  }
  .presents {
    position: absolute;
    top: 295px;
    left: 521px;
    width: 155px;
    height: 36px;
    background: linear-gradient(90deg, var(--gold-deep) 0%, var(--gold) 50%, var(--gold-light) 100%);
    color: var(--white);
    font-weight: 600;
    font-size: 18px;
    letter-spacing: 1.5px;
    line-height: 36px;
    text-align: center;
  }
  .event {
    position: absolute;
    top: 384px;
    left: 0;
    width: 100%;
    text-align: center;
  }
  .event-title {
    font-family: "Playfair Display", serif;
    font-weight: 800;
    font-size: 54px;
    line-height: 1.1;
    letter-spacing: 2px;
  }
  .event-date {
    margin-top: 14px;
    font-weight: 300;
    font-size: 58px;
    line-height: 1;
    letter-spacing: 1px;
  }
  .ornament {
    position: absolute;
    left: 0;
    top: 570px;
    width: 480px;
    height: 630px;
  }
  .lineup {
    position: absolute;
    left: 603px;
    width: 464px;
  }
  .lineup.club { top: 620px; }
  .lineup.lounge { top: 826px; }
  .stage-name {
    font-family: "Playfair Display", serif;
    font-weight: 700;
    font-size: 44px;
    line-height: 1;
    letter-spacing: 1px;
  }
  .stage-rule {
    display: block;
    margin-top: 16px;
    width: 464px;
    height: 10px;
  }
  .acts {
    list-style: none;
    margin-top: 30px;
  }
  .acts li {
    font-weight: 500;
    font-size: 22px;
    letter-spacing: 1px;
    line-height: 39px;
    color: var(--ink-soft);
  }
  .footer {
    position: absolute;
    right: 72px;
    top: 1078px;
    text-align: right;
    font-weight: 400;
    font-size: 18px;
    letter-spacing: 1.4px;
    line-height: 25px;
    color: var(--ink-soft);
  }
</style>
</head>
<body>
  <main class="flyer">
    <header class="brand">
      <div class="brand-name">QUILLFERN</div>
      <div class="brand-tagline">NIGHTCLUB + LOUNGE</div>
    </header>

    <div class="divider"></div>
    <div class="presents">PRESENTS</div>

    <section class="event">
      <h1 class="event-title">SPLIT DECK WEDNESDAY</h1>
      <p class="event-date">Nov 29 2018</p>
    </section>

    <svg class="ornament" viewBox="0 0 480 630" role="img" aria-label="Gold mandala ornament, partially off the lower left edge">
      <defs>
        <radialGradient id="mandalaTone" cx="50%" cy="50%" r="50%">
          <stop offset="0%" stop-color="#d8b47e" stop-opacity="0.55"/>
          <stop offset="60%" stop-color="#cfa870" stop-opacity="0.45"/>
          <stop offset="100%" stop-color="#c9a06a" stop-opacity="0.25"/>
        </radialGradient>
      </defs>
      <circle cx="72" cy="345" r="330" fill="url(#mandalaTone)"/>
    </svg>

    <section class="lineup club">
      <h2 class="stage-name">Club Floor</h2>
      <svg class="stage-rule" viewBox="0 0 464 10" aria-hidden="true">
        <line x1="0" y1="5" x2="440" y2="5" stroke="#b9a88f" stroke-width="1.2"/>
        <circle cx="450" cy="5" r="3.5" fill="none" stroke="#b9a88f" stroke-width="1.2"/>
      </svg>
      <ul class="acts">
        <li>GORDY B2B RALPH</li>
        <li>THEODORE BRUSKVIK</li>
      </ul>
    </section>

    <section class="lineup lounge">
      <h2 class="stage-name">Lounge</h2>
      <svg class="stage-rule" viewBox="0 0 464 10" aria-hidden="true">
        <line x1="0" y1="5" x2="440" y2="5" stroke="#b9a88f" stroke-width="1.2"/>
        <circle cx="450" cy="5" r="3.5" fill="none" stroke="#b9a88f" stroke-width="1.2"/>
      </svg>
      <ul class="acts">
        <li>OTIS B2B HALF TIDE</li>
        <li>COPPER FENWICK</li>
      </ul>
    </section>

    <footer class="footer">
      <div>POWERED BY HALVERN ACOUSTICS</div>
      <div>4716 LARCHMERE AVENUE 21+ 9PM-2AM</div>
      <div>QUILLFERNVENUE-EXAMPLE.COM FOR VIP BOOTH INQUIRIES</div>
    </footer>
  </main>
</body>
</html>
```